Stylish Business Cards Wanted

- DOUBLE SIDED Design Required -

High end, edgy cards for a corporate and personal stylist. Must include logo,
Name: Belinda Forsey
Title: Director and Stylist
telephone : +61 8 8217 4592
email: belinda@thegarbledger.example
website: thegarbledger.example
Tag: Corporate Workwear & Uniform Specialist | Personal Stylist
Would like nice icons for telephone, email, website

Target Market(s)

Businesses wanting stylish uniforms, people wanting stylish wardrobes

Industry/Entity Type

Corporate Workwear Stylist

Contact Information for Business Card

I would like black, white and gold foiling incorporated in the design - possibly a touch of the other colours on my branding guide attached Name: Belinda Forsey Title: Director and Stylist telephone : +61 8 8217 4592 email: belinda@thegarbledger.example website: thegarbledger.example Tag: Corporate Workwear & Uniform Specialist | Personal Stylist Would like nice icons for telephone, email, website

Font styles to use
Other font styles liked:
• Raleway

Colors

Designer to choose colors to be used in the design.

Requirements
Must have
• Gold foil accents

```html
<!DOCTYPE html>
<html lang="en">
<head>
<meta charset="utf-8">
<title>The Garb Ledger — Business Cards</title>
<link rel="stylesheet" href="https://fonts.googleapis.com/css2?family=Raleway:wght@300;400;600&display=swap">
<style>
  :root {
    --backdrop: #ececec;
    --ink: #231f20;
    --gold: #e3bb53;
    --paper: #ffffff;
    --rule: #8a8a8a;
  }
  * { margin: 0; padding: 0; box-sizing: border-box; }
  html, body {
    width: 1200px; height: 507px; overflow: hidden;
    background: var(--backdrop);
    font-family: "Raleway", sans-serif;
  }
  .canvas { position: relative; width: 1200px; height: 507px; }

  .card {
    position: absolute; top: 106px;
    width: 493px; height: 296px;
    overflow: hidden;
  }

  /* Front */
  .card--front { left: 83px; background: var(--ink); }
  .card--front .brand-name {
    position: absolute; left: 0; right: 0; top: 108px;
    text-align: center;
    font-weight: 400; font-size: 32px; letter-spacing: 0.06em;
    color: var(--gold);
  }
  .card--front .tagline {
    position: absolute; left: 0; right: 0; top: 220px;
    text-align: center;
    font-weight: 300; font-size: 14.5px;
    color: var(--gold);
    white-space: nowrap;
  }
  .card--front .tagline .divider { margin: 0 5px; }
  .card--front .foot-band {
    position: absolute; left: 0; right: 0; bottom: 0; height: 30px;
    background: var(--gold);
  }

  /* Back */
  .card--back { left: 624px; background: var(--paper); }
  .name-marker {
    position: absolute; left: 0; top: 35px; width: 29px; height: 49px;
    background: var(--gold);
  }
  .person-name {
    position: absolute; left: 41px; top: 34px;
    font-weight: 600; font-size: 27px; line-height: 1;
    color: var(--gold);
  }
  .person-title {
    position: absolute; left: 41px; top: 63px;
    font-weight: 400; font-size: 14px;
    color: var(--ink);
  }
  .card--back .brand-name {
    position: absolute; left: 30px; width: 175px; top: 180px;
    text-align: center;
    font-weight: 400; font-size: 21px; letter-spacing: 0.05em; line-height: 1.2;
    color: var(--ink);
  }
  .contact-rule {
    position: absolute; left: 215px; top: 192px; width: 1px; height: 69px;
    background: var(--rule);
  }
  .contact-list {
    position: absolute; left: 221px; top: 196px;
    list-style: none;
  }
  .contact-list li {
    display: flex; align-items: center;
    height: 22px;
    font-weight: 400; font-size: 14.5px;
    color: var(--ink);
  }
  .contact-list .icon { width: 11px; height: 11px; margin-right: 6px; flex: none; }
</style>
</head>
<body>
<div class="canvas">

  <section class="card card--front">
    <div class="brand-name">THE GARB LEDGER</div>
    <p class="tagline">Corporate Workwear<span class="divider">|</span>Uniform Specialist<span class="divider">|</span>Personal Stylist</p>
    <div class="foot-band"></div>
  </section>

  <section class="card card--back">
    <div class="name-marker"></div>
    <h1 class="person-name">Belinda Forsey</h1>
    <p class="person-title">Director and Stylist</p>

    <div class="brand-name">THE GARB<br>LEDGER</div>

    <div class="contact-rule"></div>
    <ul class="contact-list">
      <li>
        <svg class="icon" viewBox="0 0 12 12" aria-hidden="true">
          <circle cx="6" cy="6" r="6" fill="var(--gold)"/>
          <path d="M3.2 5.2 Q6 3.4 8.8 5.2 L8.3 6 L7.2 5.6 L7.2 5 Q6 4.6 4.8 5 L4.8 5.6 L3.7 6 Z M4.2 6.4 H7.8 V8.4 H4.2 Z" fill="#fff"/>
        </svg>
        +61 8 8217 4592
      </li>
      <li>
        <svg class="icon" viewBox="0 0 12 12" aria-hidden="true">
          <circle cx="6" cy="6" r="6" fill="var(--gold)"/>
          <rect x="3" y="4" width="6" height="4.2" fill="#fff"/>
          <path d="M3 4 L6 6.4 L9 4" fill="none" stroke="var(--gold)" stroke-width="0.7"/>
        </svg>
        belinda@thegarbledger.example
      </li>
      <li>
        <svg class="icon" viewBox="0 0 12 12" aria-hidden="true">
          <circle cx="6" cy="6" r="6" fill="var(--gold)"/>
          <g fill="none" stroke="#fff" stroke-width="0.7">
            <circle cx="6" cy="6" r="3.2"/>
            <ellipse cx="6" cy="6" rx="1.4" ry="3.2"/>
            <path d="M2.8 6 H9.2 M3.3 4.4 H8.7 M3.3 7.6 H8.7"/>
          </g>
        </svg>
        thegarbledger.example
      </li>
    </ul>
  </section>

</div>
</body>
</html>
```